Business Card Design Project

HI! Can you design a business card with the logo you designed for me? I don't know what the typical order is so can you place it in the order most people do? White background and also play with a couple of colored backgrounds. Thank you!

Darnette Ruval-Koskin
darnette@sunmorrowcoaching.com
sunmorrowcoaching.com
555-317-4082

Target Market(s)

Women

Industry/Entity Type

Business

```html
<!DOCTYPE html>
<html lang="en">
<head>
<meta charset="UTF-8">
<title>Sunmorrow Coaching Services – Business Card</title>
<link rel="stylesheet" href="https://fonts.googleapis.com/css2?family=Roboto+Condensed:wght@400;700&display=swap">
<style>
  :root {
    --card-red: #c8202f;
    --card-red-soft: #d23a47;
    --brand-orange: #f39a1e;
    --paper: #ffffff;
    --ink-white: #ffffff;
    --ink-pink: #fbe3e5;
  }
  html, body {
    margin: 0;
    padding: 0;
    width: 1200px;
    height: 720px;
    overflow: hidden;
    background: var(--paper);
  }
  .business-card {
    position: relative;
    width: 1200px;
    height: 720px;
    font-family: "Roboto Condensed", "Arial Narrow", sans-serif;
    background: var(--paper);
    overflow: hidden;
  }
  .brand-side {
    position: absolute;
    left: 0;
    top: 0;
    width: 609px;
    height: 720px;
    display: flex;
    flex-direction: column;
    align-items: center;
    justify-content: center;
  }
  .brand-mark {
    width: 116px;
    height: 116px;
    border-radius: 50%;
    background: var(--brand-orange);
    margin-bottom: 34px;
    margin-top: -40px;
  }
  .brand-name {
    margin: 0;
    text-align: center;
    color: var(--card-red);
    font-weight: 700;
    line-height: 1;
  }
  .brand-name .brand-word {
    display: block;
    font-size: 66px;
  }
  .brand-name .brand-tagline {
    display: block;
    font-size: 28px;
    letter-spacing: 5px;
    margin-top: 14px;
  }
  .contact-side {
    position: absolute;
    left: 609px;
    top: 0;
    width: 591px;
    height: 720px;
    background: var(--card-red);
    overflow: hidden;
  }
  .contact-side .backdrop-disc {
    position: absolute;
    left: 30px;
    top: -80px;
    width: 330px;
    height: 330px;
    border-radius: 50%;
    background: var(--card-red-soft);
    opacity: 0.55;
  }
  .contact-block {
    position: absolute;
    left: 87px;
    top: 432px;
    color: var(--ink-white);
  }
  .person-name {
    margin: 0 0 22px;
    font-size: 49px;
    font-weight: 700;
    letter-spacing: 0.3px;
  }
  .contact-list {
    margin: 0;
    padding: 0;
    list-style: none;
    font-size: 26px;
    line-height: 40px;
    color: var(--ink-pink);
  }
  .contact-list .label {
    font-weight: 700;
    color: var(--ink-white);
  }
</style>
</head>
<body>
  <main class="business-card">
    <section class="brand-side">
      <div class="brand-mark" aria-hidden="true"></div>
      <h1 class="brand-name">
        <span class="brand-word">Sunmorrow</span>
        <span class="brand-tagline">COACHING SERVICES</span>
      </h1>
    </section>
    <section class="contact-side">
      <div class="backdrop-disc" aria-hidden="true"></div>
      <div class="contact-block">
        <h2 class="person-name">Darnette Ruval-Koskin</h2>
        <ul class="contact-list">
          <li><span class="label">Email:</span> darnette@sunmorrowcoaching.com</li>
          <li><span class="label">Web:</span> sunmorrowcoaching.com</li>
          <li><span class="label">Phone:</span> 555-317-4082</li>
        </ul>
      </div>
    </section>
  </main>
</body>
</html>
```